Premium men's gut health supplement needs a bottle label designed

We’re velnora - a premium men’s wellness brand focused on gut health. Our first product is a high-quality daily supplement designed to support digestion, regularity, and internal cleanliness. Backed by science and tailored for modern lifestyles, velnora is crafted in the UK and proudly LGBT-owned. It aims to resolve intimacy problems that gay men may experience due to poor digestion but also does not exclude any other orientation - other men may use it simply to improve their digestion.

velnora is for health-conscious men who value science-backed supplements and want to feel confident from the inside out. Many of our early adopters will be gay and bisexual men who prioritise gut health as part of their self-care, sexual, and hygiene routine, though the product is equally effective and appealing to anyone seeking premium digestive support.

The product is premium the target customer is male, not specific to one location but primary markets will be US, UK and EU.

I’d like a supplement bottle designed for velnora, our premium men’s gut health brand. The focus should be clean, slightly clinical, and minimal - inspired by brands like Quelrin and Darvo. The key element is the wordmark (velnora) on the front, with no additional logo or icon. Lowercase text and a strong, contemporary font are preferred.

The bottle should be aesthetically pleasing so that people are proud to display it on their shelf, instead of hiding it in a cupboard (like Quelrin, darvo, Pia Venturek, Morvanel etc)

Avoid anything that shows the product as being for LGBT, e.g., no rainbows, men holding hands etc.

The design should be premium, minimalist and not be busy or overwhelming.

I have uploaded a file called "Bottle" to give an idea of the type of container, but please ignore the colours and change as you see fit. This is just for reference for the type of bottle we'll use - all colours are customisable.

I have also uploaded some images for "style" reference, e.g., darvo, quelrin, pia venturek, etc for inspiration.

```html
<!DOCTYPE html>
<html lang="en">
<head>
<meta charset="utf-8">
<title>velnora — gut health label</title>
<link rel="stylesheet" href="https://fonts.googleapis.com/css2?family=Inter:wght@300;400;700&display=swap">
<style>
  :root {
    --page-bg: #efefef;
    --label-bg: #e5e5e5;
    --ink: #1e1e1e;
    --body-ink: #3a3a3a;
    --band: #4f62a6;
    --band-text: #f4f5fb;
  }
  * { margin: 0; padding: 0; box-sizing: border-box; }
  html, body {
    width: 1200px;
    height: 900px;
    overflow: hidden;
    background: var(--page-bg);
  }
  .canvas {
    position: relative;
    width: 1200px;
    height: 900px;
    font-family: "Inter", Arial, sans-serif;
  }
  .label {
    position: absolute;
    left: 338px;
    top: 140px;
    width: 523px;
    height: 620px;
    background: var(--label-bg);
  }
  .wordmark {
    position: absolute;
    left: 50px;
    top: 38px;
    font-size: 66px;
    font-weight: 700;
    letter-spacing: -0.035em;
    line-height: 1;
    color: var(--ink);
  }
  .category-band {
    position: absolute;
    left: 0;
    top: 125px;
    width: 100%;
    height: 64px;
    background: var(--band);
    display: flex;
    align-items: center;
    padding-left: 50px;
  }
  .category-band span {
    font-size: 31px;
    font-weight: 300;
    letter-spacing: -0.02em;
    color: var(--band-text);
  }
  .description {
    position: absolute;
    left: 49px;
    top: 280px;
    width: 450px;
    font-size: 30px;
    font-weight: 300;
    letter-spacing: -0.03em;
    line-height: 40px;
    color: var(--body-ink);
  }
  .volume {
    position: absolute;
    left: 47px;
    top: 540px;
    font-size: 30px;
    font-weight: 300;
    letter-spacing: -0.03em;
    color: var(--body-ink);
  }
</style>
</head>
<body>
  <main class="canvas">
    <section class="label">
      <h1 class="wordmark">velnora</h1>
      <div class="category-band"><span>gut health</span></div>
      <p class="description">Lorem ipsum dolor sit amet, consectetur adipiscing elit, sed do eiusmod tempor incididunt ut</p>
      <p class="volume">190ml / 6.4 FL oz</p>
    </section>
  </main>
</body>
</html>
```